Wedding Ceremony Equipment Hire Business Card

I need a business card design for a new business I created called Vow Outfitters. We hire out Wedding Ceremony equipment and decorations mainly for beach and garden wedding ceremonies that include delivery, set up and dismantle. We do offer DIY Chair Hire as well.
I'd like to have a similar design and colours to our website:
www.vowoutfitters-example.com.au
If possible would like the front to incorporate our information and logo and the back to have two faded example pictures of our wedding ceremonies.
I have attached two photos and our logo. Please let me know if you need a better pic of our logo though.

Target Market(s)

Newly engaged couples, aged 25 and upwards

Industry/Entity Type

Wedding

Contact Information for Business Card

Vow Outfitters
Merel Thorpe
0491 870 264
vowoutfitters@mailbox-example.com
www.social-example.com/VowOutfitters

```html
<!DOCTYPE html>
<html lang="en">
<head>
<meta charset="utf-8">
<title>Vow Outfitters – Business Card</title>
<link rel="stylesheet" href="https://fonts.googleapis.com/css2?family=Cinzel:wght@400;700&display=swap">
<style>
  :root {
    --page: #f1f1f1;
    --mint: #9ccfbd;
    --mint-soft: #cfe9df;
    --ink: #1f2421;
    --icon: #4a4f4c;
    --white: #ffffff;
  }
  * { margin: 0; padding: 0; box-sizing: border-box; }
  html, body {
    width: 1200px; height: 900px; overflow: hidden;
    background: var(--page);
    font-family: "Cinzel", Georgia, serif;
    color: var(--ink);
  }
  .stage {
    position: relative; width: 1200px; height: 900px;
    display: flex; align-items: center; justify-content: center; gap: 50px;
  }
  .card {
    width: 520px; height: 310px; border-radius: 6px;
    position: relative; overflow: hidden;
    box-shadow: 0 4px 14px rgba(0,0,0,0.12);
  }
  /* Front */
  .card--front {
    background: var(--mint);
    display: flex; flex-direction: column; align-items: center;
    padding-top: 60px; text-align: center;
  }
  .brand-name {
    font-weight: 700; font-size: 34px; letter-spacing: 1px; color: var(--ink);
  }
  .contact-name {
    margin-top: 30px; font-size: 24px; font-weight: 400; letter-spacing: 1px;
  }
  .contact-phone { margin-top: 6px; font-size: 17px; }
  .contact-lines {
    margin-top: 12px; display: flex; flex-direction: column; align-items: center; gap: 6px;
    font-size: 12.5px; text-transform: uppercase; letter-spacing: 0.3px;
  }
  .contact-item { display: flex; align-items: center; gap: 6px; }
  .contact-item svg { width: 14px; height: 14px; flex: none; }
  /* Back */
  .card--back {
    background: var(--white);
    display: flex; gap: 12px; padding: 16px;
  }
  .back-pattern {
    position: absolute; inset: 0;
    background: linear-gradient(135deg, var(--mint-soft) 0%, var(--white) 45%, var(--white) 60%, var(--mint-soft) 100%);
  }
  .photo {
    position: relative; flex: 1; border-radius: 12px; overflow: hidden;
  }
  .photo--beach {
    background: linear-gradient(180deg, #3c6fb7 0%, #5d8cc4 35%, #eeeeee 50%, #c9a778 70%, #b48a5a 100%);
  }
  .photo--garden {
    background: linear-gradient(180deg, #6d6a4f 0%, #4e5b34 35%, #e8ece6 60%, #7a9a3c 100%);
  }
  .photo-brand {
    position: absolute; top: 20px; right: 16px;
    font-weight: 700; font-size: 16px; color: var(--white);
  }
</style>
</head>
<body>
<main class="stage">
  <section class="card card--front" aria-label="Card front">
    <h1 class="brand-name">Vow Outfitters</h1>
    <p class="contact-name">Merel Thorpe</p>
    <p class="contact-phone">0491 870 264</p>
    <div class="contact-lines">
      <div class="contact-item">
        <svg viewBox="0 0 14 14" aria-hidden="true"><circle cx="7" cy="7" r="7" fill="var(--icon)"/><rect x="3.5" y="4.5" width="7" height="5" fill="none" stroke="#fff" stroke-width="1"/><path d="M3.5 4.5 L7 7.5 L10.5 4.5" fill="none" stroke="#fff" stroke-width="1"/></svg>
        <span>vowoutfitters@mailbox-example.com</span>
      </div>
      <div class="contact-item">
        <svg viewBox="0 0 14 14" aria-hidden="true"><circle cx="7" cy="7" r="7" fill="var(--icon)"/></svg>
        <span>www.social-example.com/VowOutfitters</span>
      </div>
      <div class="contact-item">
        <svg viewBox="0 0 14 14" aria-hidden="true"><circle cx="7" cy="7" r="7" fill="var(--icon)"/><circle cx="7" cy="7" r="3.6" fill="none" stroke="#fff" stroke-width="1"/><path d="M3.4 7 H10.6 M7 3.4 V10.6" stroke="#fff" stroke-width="0.8"/></svg>
        <span>www.vowoutfitters-example.com.au</span>
      </div>
    </div>
  </section>

  <section class="card card--back" aria-label="Card back">
    <div class="back-pattern" role="img" aria-label="Soft mint decorative flourish pattern"></div>
    <div class="photo photo--beach" role="img" aria-label="Photo of white ceremony chairs set out on a beach with flowers on the aisle">
      <span class="photo-brand">Vow Outfitters</span>
    </div>
    <div class="photo photo--garden" role="img" aria-label="Photo of white ceremony chairs on a garden lawn beside a pergola"></div>
  </section>
</main>
</body>
</html>
```